Tall Market Web Design - For local online shopping 'village'

URGENTLY REQUIRE WEB DESIGNER FOR TALL MARKET WEB STORE - CODING REQUIRED

REQUIREMENT; BE ABLE TO TALK ENGLISH VERY WELL AS THIS WILL BE AN ON GOING PROJECT

(WE WILL BE TALKING ON TALKWAVE OR CHATLINE)

The business name is 'Wolvendorp's - Illawarra's Online Shopping Village'
(PICS ATTACHED FOR LAYOUT DEMONSTRATION PURPOSES)

I need a draft of the website operational within 7 days to show potential clients. The remainder may take an additional 7+ days to complete. Can discuss further payments due to the work involved.

It's an online shopping village where individual shop owners have the ability to place their store (logo) and their products on this website to increase exposure to their business and more importantly their online delivery service.

The site will need to be structured in a very easy to use manner. Customers ages will range from 18+ to 80+.

THE IMAGINATION, FEEL & PRESENCE OF THE WEB PAGE;
You are a professional web designer, I will need you to use your imagination and add pieces to this website that I can't see. My vision and feel for this website is based on the grocery stores that were able to survive and thrive during the late stages of WWII. A lot of design now and with future marketing & advertising will be revolved and the 1940's feel & look. I'm happy to hear your thoughts on things we can add or improve on in the site. It's very basic now and it's more warmth and character.

THE LAYOUT;
The first page will have a white brick wallpaper background (pic attached as 'wallpaper'. This will be the wallpaper used for the entire site. The business logo (hasn't been made yet - waiting on drafts) will be at the top of the page and beneath it will be 3 categories to choose from (in the final stage it will have 6 categories).

DRAFT STAGE;
1. Village grocers (pic attached ' vgrocers') (To be written ' Village Grocers written on the frame burnt into the wood or written underneath the frame - must be large and clear to read')
2. Butchers (pic attached 'vbutcher')(as above - Village butchers)
3. Seafood (pic attached 'VSF')(as above Seafood)
They will all require framing (pic attached 'frame')
I'd like the images to be slightly bouncy if you put your mouse or finger on the logo.

Once the customer enters their choice it will then take them to their desired category.

NEXT PAGE:

Main focus is in the Grocers section; The same design structure will appear (business logo 'Wolvendorp - Illawarra's online shopping village'.
2 business choices will be available in this section. Their logos are attached ('PQHN' and 'Hobson's Grocer') I'd like you to enhance the logo's with more depth and background shadow - please don't spend to much time but make them look better. I'd like the logo's to be slightly bouncy if you put your mouse or finger on the logo. The wallpaper used will be 'wallpaper'.

PLEASE NOTE: Could you please remove the logo from the background image of 'PQHN'.

For the draft stage we will focus on 'PQHN'. Once you click on PQHN it will take you to their page. The wallpaper will be the same as the brick wallpaper on the other 2 pages. The logo of 'PQHN' will be placed boldly at the top middle of the page. On this page there will be 4 categories to choose from. Everything will be the same, wallpaper will be white brick, the categories (pics attached as Deli, Fruit&Veg, Bakery & Pantry ) they will need to be framed and the category name will be burnt into the wood or placed underneath.

This is where we stop for the time being.

I've attached layout pictures, so you can see what I see. Please add all the little things i've added to the layout pictures that i haven't written here..

Example: Our Mission, Contact us, Home delivery.. etc.

The site will need to continue to grow as we fill the categories with products and add more businesses to the site.. so on and so on. It's an ongoing job and we will need good communication and understanding with each other.

Please do what you can to show your vision in line with what i've written above. If you'd like to contact me feel free to do so, we can organize a talk on talkwave if need be.

All the best & I hope you are all safe and healthy!

Dunn

Industry/Entity Type

Online Store

Coding

Coded - Design and coding required

Number of Pages Required

5+ page

Requirements
Must have
• Looks like the 1940's merged with the modern age.
Nice to have
• Age some nice grocery store touches. 1940's + grocery stores had things hanging from the walls, ornaments here and there. It felt homely. Add some things or talk about the things that you're thinking about adding.

```html
<!DOCTYPE html>
<html lang="en">
<head>
<meta charset="utf-8">
<title>Wolvendorp's – Illawarra's Online Shopping Village</title>
<link rel="stylesheet" href="https://fonts.googleapis.com/css2?family=Oswald:wght@400;500;600;700&family=Open+Sans:wght@400&display=swap">
<style>
:root{
  --ink:#111111;
  --ink-soft:#2a2a2a;
  --wall:#f0f0ef;
  --wall-shade:#e4e4e2;
  --bar:#000000;
  --white:#ffffff;
  --wood-dark:#5a3413;
  --wood:#8a5528;
  --wood-light:#a86c36;
  --footer-band:#bfbfbf;
}
*{box-sizing:border-box;margin:0;padding:0}
html,body{width:988px;height:1200px;overflow:hidden}
body{
  position:relative;
  font-family:'Oswald',sans-serif;
  color:var(--ink);
  background:linear-gradient(180deg,var(--wall) 0%,var(--wall-shade) 50%,var(--wall) 100%);
}
.abs{position:absolute}

/* promo bar */
.promo-bar{left:0;top:0;width:988px;height:26px;background:var(--bar);color:var(--white);
  font-size:12px;letter-spacing:.6px;display:flex;align-items:center;justify-content:center}

/* header */
.nav-link{top:66px;font-size:15px;font-weight:500;letter-spacing:.6px;color:var(--ink-soft);text-decoration:none}
.nav-link.is-active{border-bottom:2px solid var(--ink-soft);padding-bottom:3px}
.brand{left:336px;width:300px;top:52px;text-align:center}
.brand-name{font-size:40px;font-weight:700;letter-spacing:1.5px;line-height:1}
.header-icon{top:66px}
.cart-count{left:916px;top:60px;width:17px;height:17px;border-radius:50%;background:var(--ink);
  color:var(--white);font-size:10px;font-weight:700;display:flex;align-items:center;justify-content:center}

/* wooden frames */
.frame{background:linear-gradient(180deg,var(--wood-light),var(--wood) 45%,var(--wood-dark));
  border-radius:4px;box-shadow:0 3px 6px rgba(0,0,0,.35)}
.frame-rail{background:linear-gradient(180deg,var(--wood-light),var(--wood) 60%,var(--wood-dark));
  border-radius:3px;box-shadow:0 2px 4px rgba(0,0,0,.3)}

/* hero */
.hero-photo{left:92px;top:163px;width:793px;height:398px;
  background:radial-gradient(ellipse at 50% 50%,#4a3a2a 0%,#2f261d 60%,#231c15 100%)}
.hero-title{left:92px;width:793px;top:300px;text-align:center;color:var(--white)}
.hero-title h1{font-size:48px;font-weight:600;letter-spacing:3px;line-height:1.05}
.hero-title p{font-size:25px;font-weight:500;letter-spacing:2px;margin-top:2px}
.hero-arrow{top:326px}

/* categories */
.category-photo{height:132px}
.category-label{top:856px;width:272px;text-align:center;font-size:21px;font-weight:600;letter-spacing:1.2px}

/* divider */
.divider{left:61px;top:925px;width:864px;height:20px}

/* footer */
.footer-heading{top:980px;font-size:18px;font-weight:600;letter-spacing:.8px}
.footer-link{font-size:12.5px;letter-spacing:.5px;color:var(--ink)}
.footer-brand{left:366px;width:260px;top:980px;text-align:center}
.footer-brand .brand-name{font-size:31px}
.email-field{left:658px;top:1010px;width:197px;height:36px;border:1.5px solid var(--ink);
  background:var(--white);font-size:11px;letter-spacing:.6px;color:#555;padding:0 13px;display:flex;align-items:center}
.go-button{left:862px;top:1010px;width:42px;height:36px;background:var(--ink);color:var(--white);
  font-size:17px;font-weight:600;display:flex;align-items:center;justify-content:center}
.social{top:1070px;display:flex;align-items:center;gap:5px;font-size:11px;font-weight:500;letter-spacing:.5px}
.social-mark{width:9px;height:9px;background:var(--ink)}
.copyright-band{left:0;top:1152px;width:988px;height:48px;background:var(--footer-band);
  font-family:'Open Sans',sans-serif;font-size:12px;color:#222;display:flex;align-items:center;justify-content:center}
</style>
</head>
<body>

<div class="abs promo-bar">GET 10% OFF SALE ON NEW CUSTOMERS</div>

<header>
  <a class="abs nav-link is-active" style="left:105px">ABOUT</a>
  <a class="abs nav-link" style="left:178px">MISSION</a>
  <a class="abs nav-link" style="left:261px">PRODUCT</a>
  <div class="abs brand">
    <div class="brand-name">WOLVENDORP'S</div>
  </div>
  <a class="abs nav-link" style="left:658px">HOME DELVIERY</a>
  <a class="abs nav-link" style="left:785px">CONTACT</a>
  <svg class="abs header-icon" style="left:872px" width="14" height="17" viewBox="0 0 14 17" fill="none" stroke="#333" stroke-width="1.2" aria-label="Account">
    <circle cx="7" cy="5" r="3.6"/><path d="M1 16v-2.5a6 6 0 0 1 12 0V16z"/>
  </svg>
  <svg class="abs header-icon" style="left:898px" width="20" height="17" viewBox="0 0 20 17" fill="none" stroke="#333" stroke-width="1.2" aria-label="Cart">
    <path d="M1 2h3l2.5 9h10l2-7H5"/><circle cx="8" cy="14.5" r="1.4"/><circle cx="15" cy="14.5" r="1.4"/>
  </svg>
  <div class="abs cart-count">0</div>
</header>

<section class="hero">
  <div class="abs frame" style="left:56px;top:122px;width:870px;height:478px"></div>
  <div class="abs frame-rail" style="left:46px;top:126px;width:884px;height:36px"></div>
  <div class="abs frame-rail" style="left:48px;top:560px;width:882px;height:36px"></div>
  <div class="abs hero-photo" role="img" aria-label="Fresh vegetables on a dark wooden table: lettuce, beans, tomatoes, capsicums, broccoli and radishes"></div>
  <div class="abs hero-title">
    <h1>WELCOME TO WOLVENDORP'S</h1>
    <p>ILLAWARRA'S ONLINE SHOPPING VILLAGE</p>
  </div>
  <svg class="abs hero-arrow" style="left:107px" width="16" height="26" viewBox="0 0 16 26" fill="none" stroke="#fff" stroke-width="3"><path d="M14 2 3 13l11 11"/></svg>
  <svg class="abs hero-arrow" style="left:864px" width="16" height="26" viewBox="0 0 16 26" fill="none" stroke="#fff" stroke-width="3"><path d="M2 2l11 11L2 24"/></svg>
</section>

<section class="categories">
  <div class="abs frame" style="left:56px;top:644px;width:266px;height:200px"></div>
  <div class="abs frame-rail" style="left:53px;top:648px;width:272px;height:30px"></div>
  <div class="abs frame-rail" style="left:55px;top:811px;width:270px;height:32px"></div>
  <div class="abs category-photo" style="left:91px;top:679px;width:197px;background:linear-gradient(135deg,#2a2a2a,#5b6b2e 45%,#a24a2a 75%,#2a2a2a)" role="img" aria-label="Crate of fresh fruit and vegetables"></div>
  <div class="abs category-label" style="left:53px">VILLAGE GROCERS</div>

  <div class="abs frame" style="left:359px;top:644px;width:266px;height:200px"></div>
  <div class="abs frame-rail" style="left:356px;top:648px;width:272px;height:30px"></div>
  <div class="abs frame-rail" style="left:358px;top:811px;width:270px;height:32px"></div>
  <div class="abs category-photo" style="left:394px;top:679px;width:197px;background:linear-gradient(180deg,#b98a88,#8a5a52 45%,#2a2624)" role="img" aria-label="Raw cuts of meat on wooden boards"></div>
  <div class="abs category-label" style="left:356px">BUTCHERS</div>

  <div class="abs frame" style="left:662px;top:644px;width:266px;height:200px"></div>
  <div class="abs frame-rail" style="left:659px;top:648px;width:271px;height:30px"></div>
  <div class="abs frame-rail" style="left:661px;top:811px;width:269px;height:32px"></div>
  <div class="abs category-photo" style="left:697px;top:679px;width:197px;background:linear-gradient(135deg,#c9c5c8,#9a7e86 40%,#6a7886 70%,#c8b0a8)" role="img" aria-label="Fresh seafood on ice: octopus, lobster, fish and shellfish"></div>
  <div class="abs category-label" style="left:659px">SEAFOODS</div>
</section>

<svg class="abs divider" viewBox="0 0 864 20" fill="none" stroke="#222">
  <line x1="0" y1="8" x2="420" y2="8" stroke-width="1"/>
  <line x1="0" y1="12" x2="420" y2="12" stroke-width="1"/>
  <line x1="456" y1="8" x2="864" y2="8" stroke-width="1"/>
  <line x1="456" y1="12" x2="864" y2="12" stroke-width="1"/>
  <path d="M438 1 447 10 438 19 429 10z" stroke-width="2"/>
</svg>

<footer>
  <div class="abs footer-heading" style="left:85px">QUICK LINKS</div>
  <div class="abs footer-link" style="left:85px;top:1015px">PRODUCTS</div>
  <div class="abs footer-link" style="left:85px;top:1040px">MISSION</div>
  <div class="abs footer-link" style="left:85px;top:1065px">HOME DELVIDERY</div>

  <div class="abs footer-heading" style="left:229px">RESOURCES</div>
  <div class="abs footer-link" style="left:228px;top:1015px">MY ACCOUNT</div>
  <div class="abs footer-link" style="left:228px;top:1040px">CART</div>
  <div class="abs footer-link" style="left:228px;top:1065px">CONTACT US</div>

  <div class="abs footer-brand">
    <div class="brand-name">WOLVENDORP'S</div>
  </div>

  <div class="abs footer-heading" style="left:658px">JOIN THE VILLAGE</div>
  <div class="abs email-field">EMAIL ADDRESS</div>
  <div class="abs go-button">GO</div>
  <div class="abs social" style="left:664px"><span class="social-mark"></span>FRIENDBOOK</div>
  <div class="abs social" style="left:752px"><span class="social-mark"></span>SNAPGRAM</div>

  <div class="abs copyright-band">© 2020 Company Name | All Rights Reserved</div>
</footer>

</body>
</html>
```